The Ashcombe- outdoor banner

This should be a horizontal banner. It should have the logos attached incorporated and the following details
Coming Spring 2025: The Ashcombe - Exclusive Luxury Condos
Listed by Marisol Avenell | Quillfield Realty
Construction by Pinegate Builders
Unveil the height of luxury living with The Ashcombe, a new condo building in East Boston, set for completion in Spring 2025. Experience a standard of elegance and sophistication like never before.
For more information and inquiries, please contact:
Marisol Avenell
Phone: (617) 490-7163
Email: marisol@quillfieldhomes.example
The banner should be very classy incorporting gold and navy very classic fonts. The Ashcombe should look very classy and exclusive. The pinegate builders logo should be smaller. It should not include their phone number and instagram handle only the name of the company. Herringbone pattern in the background would be great. This is going outside the building to advertise pre construction units

```html
<!DOCTYPE html>
<html lang="en">
<head>
<meta charset="utf-8">
<title>The Ashcombe – Outdoor Banner</title>
<link rel="stylesheet" href="https://fonts.googleapis.com/css2?family=Cinzel:wght@500&family=Playfair+Display:wght@900&family=Questrial&family=Jost:wght@500;600&display=swap">
<style>
  :root {
    --navy-deep: #0a0f3a;
    --navy: #16215a;
    --navy-glow: #26356e;
    --silver-light: #f4f4f6;
    --silver-dark: #9a9ca6;
    --gold-light: #fff1a6;
    --gold: #f5c53a;
    --gold-dark: #c98a14;
    --white: #ffffff;
  }
  * { margin: 0; padding: 0; box-sizing: border-box; }
  html, body {
    width: 1200px; height: 686px; overflow: hidden;
    background: #e6e6e6;
  }
  .banner {
    position: absolute; inset: 0;
    width: 1200px; height: 686px;
    background:
      linear-gradient(135deg, transparent 0 70%, rgba(255,255,255,0.035) 70% 78%, transparent 78%),
      linear-gradient(45deg, transparent 0 12%, rgba(255,255,255,0.04) 12% 20%, transparent 20% 26%, rgba(255,255,255,0.03) 26% 31%, transparent 31%),
      radial-gradient(ellipse 60% 55% at 45% 40%, var(--navy-glow) 0%, var(--navy) 45%, var(--navy-deep) 100%);
    font-family: "Questrial", sans-serif;
    color: var(--white);
  }
  .headline {
    position: absolute; left: 0; width: 1176px; top: 34px;
    text-align: center; white-space: nowrap;
    font-family: "Cinzel", serif; font-weight: 500;
    font-size: 86px; line-height: 100px; letter-spacing: 2px;
    background: linear-gradient(180deg, var(--silver-light) 30%, var(--silver-dark) 100%);
    -webkit-background-clip: text; background-clip: text; color: transparent;
    filter: drop-shadow(2px 3px 2px rgba(0,0,0,0.6));
  }
  .gold-text {
    background: linear-gradient(180deg, var(--gold-light) 0%, var(--gold) 50%, var(--gold-dark) 100%);
    -webkit-background-clip: text; background-clip: text; color: transparent;
    filter: drop-shadow(2px 3px 2px rgba(0,0,0,0.55));
    white-space: nowrap;
  }
  .title-block { position: absolute; left: 110px; width: 642px; top: 160px; text-align: center; }
  .title-rule { position: absolute; height: 2px; background: linear-gradient(90deg, var(--gold-dark), var(--gold), var(--gold-dark)); }
  .title-rule--left { left: 0; width: 250px; top: 24px; }
  .title-rule--right { right: 0; width: 270px; top: 24px; }
  .title-rule--bottom { left: 2px; right: 0; top: 216px; }
  .title-article { font-family: "Playfair Display", serif; font-weight: 900; font-size: 38px; line-height: 44px; }
  .title-name { font-family: "Playfair Display", serif; font-weight: 900; font-size: 102px; line-height: 116px; letter-spacing: 0; margin-top: 2px; }
  .title-tagline { font-family: "Playfair Display", serif; font-weight: 900; font-size: 37px; line-height: 46px; letter-spacing: 0.5px; margin-top: 4px; }

  .credit { position: absolute; text-align: center; font-family: "Jost", sans-serif; white-space: nowrap; }
  .credit-label { font-size: 14px; font-weight: 500; letter-spacing: 1px; }
  .credit-name { font-size: 18px; font-weight: 600; letter-spacing: 0.5px; margin-top: 2px; }
  .credit--listing { left: 799px; width: 220px; top: 186px; }
  .credit--builder { left: 1013px; width: 160px; top: 210px; }
  .brand-mark {
    width: 58px; height: 58px; border: 2px solid var(--white); border-radius: 50%;
    margin: 14px auto 10px;
  }
  .brand-name { font-family: "Jost", sans-serif; font-weight: 500; font-size: 18px; letter-spacing: 1px; color: var(--white); white-space: nowrap; }
  .brand-name--small { font-size: 14px; margin-top: 44px; }

  .intro {
    position: absolute; left: 0; width: 1176px; top: 406px;
    text-align: center; font-size: 26px; line-height: 34px; letter-spacing: 0.3px;
  }
  .divider {
    position: absolute; left: 140px; right: 140px; top: 536px; height: 1px;
    background: linear-gradient(90deg, transparent, rgba(255,255,255,0.12), transparent);
  }
  .contact-lead {
    position: absolute; left: 0; width: 1176px; top: 568px;
    text-align: center; font-size: 18.5px; letter-spacing: 0.3px;
  }
  .contact-row {
    position: absolute; left: 0; width: 1176px; top: 606px;
    display: flex; justify-content: center; align-items: center; gap: 14px;
    font-family: "Jost", sans-serif; font-weight: 600; font-size: 25px; letter-spacing: 0.3px;
    white-space: nowrap;
  }
  .contact-item { display: flex; align-items: center; gap: 10px; }
  .contact-icon { width: 28px; height: 28px; }
  .gold-bar {
    position: absolute; left: 0; right: 0; bottom: 0; height: 11px;
    background: linear-gradient(90deg, var(--gold-dark), var(--gold), var(--gold-light), var(--gold), var(--gold-dark));
  }
</style>
</head>
<body>
  <main class="banner">
    <h1 class="headline">COMING SPRING 2025</h1>

    <section class="title-block">
      <span class="title-rule title-rule--left"></span>
      <span class="title-rule title-rule--right"></span>
      <div class="title-article gold-text">THE</div>
      <div class="title-name gold-text">ASHCOMBE</div>
      <div class="title-tagline gold-text">EXCLUSIVE LUXURY CONDOS</div>
      <span class="title-rule title-rule--bottom"></span>
    </section>

    <section class="credit credit--listing">
      <div class="credit-label">LISTED BY</div>
      <div class="credit-name">Marisol Avenell</div>
      <div class="brand-mark"></div>
      <div class="brand-name">QUILLFIELD REALTY</div>
    </section>

    <section class="credit credit--builder">
      <div class="credit-label">CONSTRUCTION BY</div>
      <div class="brand-name brand-name--small">PINEGATE BUILDERS</div>
    </section>

    <p class="intro">
      Unveil the height of luxury living with The Ashcombe, a new condo<br>
      building in East Boston, set for completion in Spring 2025.<br>
      Experience a standard of elegance and sophistication like never before.
    </p>

    <div class="divider"></div>

    <p class="contact-lead">FOR MORE INFORMATION AND INQUIRIES, PLEASE CONTACT</p>

    <div class="contact-row">
      <span class="contact-item">MARISOL AVENELL</span>
      <span class="contact-item">
        <svg class="contact-icon" viewBox="0 0 28 28" aria-hidden="true">
          <circle cx="14" cy="14" r="12.5" fill="none" stroke="#f5c53a" stroke-width="1.6"/>
          <path d="M10 8.5l2 3-1.3 1.2c.8 1.7 2 2.9 3.6 3.6l1.2-1.3 3 2-1.2 2.2c-4.6-.4-8.300-4.1-8.6-8.6z" fill="none" stroke="#f5c53a" stroke-width="1.3" stroke-linejoin="round"/>
        </svg>
        (617) 490-7163
      </span>
      <span class="contact-item">
        <svg class="contact-icon" viewBox="0 0 28 28" aria-hidden="true">
          <circle cx="14" cy="14" r="12.5" fill="none" stroke="#f5c53a" stroke-width="1.6"/>
          <rect x="8.5" y="10" width="11" height="8" rx="1" fill="none" stroke="#f5c53a" stroke-width="1.3"/>
          <path d="M8.8 10.4l5.2 4 5.2-4" fill="none" stroke="#f5c53a" stroke-width="1.3"/>
        </svg>
        MARISOL@QUILLFIELDHOMES.EXAMPLE
      </span>
    </div>

    <div class="gold-bar"></div>
  </main>
</body>
</html>
```